Landing Page Design

We need a landing page template designed to support a clients Zenfy Bidpost Campaigns. The client is called Morlet Plumbing and they install and repair hot water systems (only). They provide no other plumbing services.

We are really looking for a great looking landing page that is both engaging and functional.

Target Market(s)

Residential/Domestic market. Typically wives and partners who are typically home or run the household.

Industry/Entity Type

Plumbing

Number of Pages Required

1 page

Requirements
Must have
• Strong branding
Strong call to actions
Great and obvious looking buttons
Nice to have
• Smart use of colour
Should not have
• The design should not use old-style, serif fonts.

Do not include any plumbing images

```html
<!DOCTYPE html>
<html lang="en">
<head>
<meta charset="utf-8">
<title>Morlet Plumbing – Hot Water Now</title>
<link rel="stylesheet" href="https://fonts.googleapis.com/css2?family=Mulish:wght@400;600;700;800&display=swap">
<style>
:root{
  --orange:#f26634;
  --orange-text:#ec6535;
  --panel-grey:#e7e5e4;
  --page-grey:#e4e2e1;
  --outer:#f1f1f1;
  --field:#e9e8e8;
  --white:#ffffff;
  --shower-light:#d9d6d5;
  --shower-dark:#8a7f7b;
}
*{box-sizing:border-box;margin:0;padding:0}
html,body{width:1200px;height:934px;overflow:hidden;background:var(--outer);font-family:"Mulish",sans-serif}
.canvas{position:relative;width:1200px;height:934px;overflow:hidden}
.frame{position:absolute;left:42px;top:0;width:1120px;height:893px;background:var(--page-grey)}
.brand-band{position:absolute;left:42px;top:120px;width:1120px;height:12px;background:var(--orange)}
.brand{position:absolute;left:72px;top:40px;width:180px;height:92px;background:var(--page-grey);display:flex;align-items:center;gap:10px;padding-left:4px}
.brand-mark{width:22px;height:22px;border-radius:50%;background:var(--orange);flex:none}
.brand-name{font-weight:800;font-size:22px;line-height:1.05;color:var(--orange)}

.offer{position:absolute;left:75px;top:165px;width:636px;height:653px;background:var(--orange)}
.offer-title{height:112px;display:flex;align-items:center;justify-content:center;gap:14px;color:var(--white)}
.offer-title h1{font-weight:700;font-size:54px;letter-spacing:-0.5px}
.offer-title span{font-weight:800;font-size:27px;margin-top:12px}
.offer-copy{position:absolute;left:7px;top:112px;width:353px;height:533px;background:var(--panel-grey);padding:28px 14px 0 14px;color:var(--orange-text)}
.offer-copy h2{font-weight:700;font-size:24px;text-align:center;margin-bottom:18px}
.offer-copy p{font-weight:700;font-size:17.5px;line-height:24px;letter-spacing:-0.2px;text-align:justify;hyphens:auto;-webkit-hyphens:auto;margin-bottom:24px}
.offer-photo{position:absolute;left:369px;top:112px;width:267px;height:541px;background:linear-gradient(160deg,var(--shower-light) 0%,#bdb4b0 45%,var(--shower-dark) 100%)}

.footer-band{position:absolute;left:42px;top:848px;width:1120px;height:45px;background:var(--orange)}

.contact{position:absolute;left:744px;top:78px;width:396px;height:815px;background:var(--orange);border-radius:16px 16px 0 0;color:var(--white)}
.contact-call{text-align:center;font-weight:700;font-size:28px;margin-top:14px}
.contact-points{text-align:center;font-weight:700;font-size:10.5px;margin-top:14px;line-height:26px;word-spacing:2px}
.contact-points span{margin:0 7px}
.contact-intro{position:absolute;left:27px;top:137px;width:345px;font-weight:700;font-size:14.5px;line-height:24px;text-align:justify;hyphens:auto;-webkit-hyphens:auto}
.contact-intro strong{font-size:19px;font-weight:800}
.field{position:absolute;left:26px;width:343px}
.field label{display:block;font-weight:700;font-size:12.5px;margin-bottom:8px}
.field input,.field textarea{display:block;width:100%;height:36px;border:0;background:var(--field);font:inherit}
.field textarea{height:93px;resize:none}

.action{position:absolute;top:868px;height:66px;width:218px;background:var(--field);border-radius:9px 9px 0 0;text-align:center;color:var(--orange-text);font-weight:700;font-size:16px;line-height:19px;padding-top:10px;text-decoration:none}
.action-primary{left:828px;width:231px;height:40px;border-radius:9px;font-size:23px;line-height:24px;padding-top:7px}
</style>
</head>
<body>
<div class="canvas">
  <div class="frame"></div>
  <div class="brand-band"></div>
  <div class="brand">
    <div class="brand-mark"></div>
    <div class="brand-name">Morlet Plumbing</div>
  </div>

  <section class="offer">
    <div class="offer-title"><h1>Hot Water Now!</h1><span>SAVE $$$</span></div>
    <div class="offer-copy">
      <h2>Solar Hot Water Systems</h2>
      <p>Engage our routine office clean&shy;ing for at least 6 months and receive a FREE Carpet and Window clean! No strings attached, no contracts.</p>
      <p>To take advantage of this great offer call us on 1300 58 17 40 or complete and submit the form on this page.</p>
      <p>At Brevia we provide all your property service needs - pain&shy;lessly. We understand that clean&shy;ing and other property services should be background activities. A set and forget proposition.</p>
    </div>
    <div class="offer-photo" role="img" aria-label="Photo of a woman enjoying a hot shower"></div>
  </section>

  <div class="footer-band"></div>

  <aside class="contact">
    <div class="contact-call">Call NOW on 9471 5038</div>
    <div class="contact-points">
      <span>Sydney 24 Hours 7 Days</span><span>On Time</span><span>Professional Technicians</span><br>
      <span>We Advise on Rebates</span><span>Authorised Kelvoran Dealer</span>
    </div>
    <p class="contact-intro">Take Advantage of this Great Offer. Con&shy;tact Us NOW on <strong>9471 5038</strong> or Register your Interest Below</p>
    <form>
      <div class="field" style="top:238px"><label style="padding-left:4px">Your First Name:</label><input type="text"></div>
      <div class="field" style="top:321px"><label>Your Surname:</label><input type="text"></div>
      <div class="field" style="top:405px"><label>Your Suburb:</label><input type="text"></div>
      <div class="field" style="top:489px"><label>Best Contact Number:</label><input type="text"></div>
      <div class="field" style="top:569px"><label>Your Email Address:</label><input type="email"></div>
      <div class="field" style="top:649px"><label>Enquiry / Comments:</label><textarea></textarea></div>
    </form>
  </aside>

  <a class="action" style="left:50px">Book a<br>FREE Quote</a>
  <a class="action" style="left:280px">Visit our<br>Website</a>
  <a class="action" style="left:511px">Click Here for Information<br>on Rebates</a>
  <a class="action action-primary">Enquire Now</a>
</div>
</body>
</html>
```